Banner & also another minor digital image for an Online Academic Journal

A direct example of what I need can be found in this webpage: http://papers.tbhu-archive.org/qrvt/
(Please see attached files, "sAMPLE", and "sAMPLE 2", so you can see what I mean.)
This link (http://papers.tbhu-archive.org/qrvt/) is for an existing ONLINE ACADEMIC JOURNAL at the Thornbury Hill University.
It will help for you to be acquainted with the format of Online Academic Journals.
You will find that there is a banner on top as well as a digital image of a journal/book cover on the right.
I need a
(1) banner and
a (2) digital journal/book cover
for a website for an ONLINE ACADEMIC JOURNAL.
I am looking for a serious, professional, elegant design.
There will not be a print version. Only web-based online publication. No coding needed, only PSD, JPG/PNG and PDF.
1) We use PelloWave (http://archives.pellowave.com/repository-software/journals/) for the digital image of the journal/book cover layout. Link shows the general layout of the journal website.
2) For the digital image of the journal/book cover and also the banner,
Name of the journal is....
"Lumen: A Quarterly of Civic Ethics and Recovery Work"
Only this text will be used and applied to both banner and cover.
***The color associated with the theme of dignity is purple
****You could also add the color red.
*****I don't want the design to be garish, but accents in red might represent
the sexual exploitation and violence in the title.
3) Attached "sAmple 2" file is a basic design for the digital image of the journal/book cover from PelloWave. I am looking for something more elegant and professional looking. Your creativity is encouraged. I am open to receiving your interpretation.
Target Market(s)
Academics & Community Professionals
Industry/Entity Type
Non Profit
Contact Information for Business Card
Match journal design

```html
<!DOCTYPE html>
<html lang="en">
<head>
<meta charset="utf-8">
<title>Lumen — Cover and Banner</title>
<link rel="stylesheet" href="https://fonts.googleapis.com/css2?family=Bebas+Neue&family=Fira+Sans:ital,wght@0,400;1,300;1,400&display=swap">
<style>
  :root {
    --ink: #2a1f3d;
    --lavender: #8f7bab;
    --violet: #6b4fa3;
    --violet-deep: #4a3673;
    --paper: #ffffff;
    --rule: #6e5f86;
  }
  * { box-sizing: border-box; margin: 0; padding: 0; }
  html, body { width: 1200px; height: 1200px; overflow: hidden; background: var(--paper); }
  body { position: relative; font-family: "Fira Sans", Arial, sans-serif; }

  .journal-cover {
    position: absolute; left: 301px; top: 46px; width: 630px; height: 890px;
    background: var(--ink); overflow: hidden;
  }
  .cover-spine-bar {
    position: absolute; left: 0; top: 92px; width: 13px; height: 690px;
    background: var(--lavender);
  }
  .cover-artwork {
    position: absolute; left: 71px; top: 434px; right: 0; bottom: 0;
    background:
      radial-gradient(ellipse 60% 55% at 62% 50%, rgba(143,123,171,0.55) 0%, rgba(107,79,163,0.45) 35%, rgba(74,54,115,0.35) 60%, rgba(42,31,61,0) 85%);
  }
  .cover-title {
    position: absolute; left: 95px; top: 70px;
    font-family: "Bebas Neue", Impact, sans-serif; font-size: 180px; line-height: 1;
    color: var(--paper); letter-spacing: 1px;
  }
  .cover-subtitle {
    position: absolute; left: 95px; top: 224px;
    font-style: italic; font-weight: 300; font-size: 40px; line-height: 47px;
    color: var(--lavender);
  }
  .cover-editor {
    position: absolute; left: 95px; top: 392px; color: var(--paper);
  }
  .editor-name { font-size: 22px; line-height: 26px; text-transform: uppercase; }
  .editor-role { font-size: 22px; line-height: 26px; font-style: italic; }
  .cover-rule {
    position: absolute; left: 95px; top: 452px; width: 228px; height: 1px; background: var(--rule);
  }
  .cover-contact {
    position: absolute; left: 95px; top: 472px;
    font-style: italic; font-size: 19px; line-height: 27px; color: var(--paper);
  }

  .journal-banner {
    position: absolute; left: 84px; top: 970px; width: 1032px; height: 188px;
    background: var(--ink); overflow: hidden;
  }
  .banner-artwork {
    position: absolute; left: 612px; top: 0; right: 0; bottom: 0;
    background:
      radial-gradient(ellipse 55% 80% at 65% 45%, rgba(143,123,171,0.55) 0%, rgba(107,79,163,0.45) 35%, rgba(74,54,115,0.3) 65%, rgba(42,31,61,0) 90%);
  }
  .banner-title {
    position: absolute; left: 54px; top: 28px;
    font-family: "Bebas Neue", Impact, sans-serif; font-size: 92px; line-height: 1;
    color: var(--paper);
  }
  .banner-subtitle {
    position: absolute; left: 245px; top: 44px;
    font-style: italic; font-weight: 300; font-size: 23px; line-height: 27px;
    color: var(--lavender);
  }
  .banner-rule {
    position: absolute; left: 54px; top: 113px; width: 520px; height: 1px; background: var(--rule);
  }
  .banner-editor {
    position: absolute; left: 54px; top: 124px; color: var(--paper);
  }
  .banner-editor .editor-name, .banner-editor .editor-role { font-size: 18px; line-height: 22px; }
  .banner-contact {
    position: absolute; left: 245px; top: 124px;
    font-style: italic; font-size: 18px; line-height: 22px; color: var(--paper);
  }
</style>
</head>
<body>

  <section class="journal-cover">
    <div class="cover-artwork" role="img" aria-label="Halftone dot field with a hand working puppet strings attached to a small human figure"></div>
    <div class="cover-spine-bar"></div>
    <h1 class="cover-title">LUMEN</h1>
    <p class="cover-subtitle">A Quarterly of<br>Civic Ethics and<br>Recovery Work</p>
    <div class="cover-editor">
      <p class="editor-name">Marian T. Okafor</p>
      <p class="editor-role">Editor-in-Chief</p>
    </div>
    <div class="cover-rule"></div>
    <p class="cover-contact">mokafor@thornbury.edu<br>www.lumenquarterly.org</p>
  </section>

  <section class="journal-banner">
    <div class="banner-artwork" role="img" aria-label="Halftone dot field with a hand working puppet strings attached to a small human figure"></div>
    <h2 class="banner-title">LUMEN</h2>
    <p class="banner-subtitle">A Quarterly of<br>Civic Ethics and Recovery Work</p>
    <div class="banner-rule"></div>
    <div class="banner-editor">
      <p class="editor-name">Marian T. Okafor</p>
      <p class="editor-role">Editor-in-Chief</p>
    </div>
    <p class="banner-contact">mokafor@thornbury.edu<br>www.lumenquarterly.org</p>
  </section>

</body>
</html>
```